Pellory Wealth Management - website refresh

www.pellorywealth-example.com. We are a UK wealth management company. The website is looking tired and old.
We would like to keep similar content ie works and overall structure, just improve the look of the website and modernise the site. Needs to be a professional financial site.
Looking for suggestions for new photos and graphics.
would like to keep plugins for the poll otter links and market lens widgets that are currently embedded.
would like to keep "our process" graphic.
"portfolio advisory service" page can go, as no longer applicable.
the "client log in" tab can link to this, our new back office system https://pellorywm.gb.vxq-example.net/
Would like colours that work with logo
like images and styles of these sites, same target market
https://www.tindalforsyth-example.com/
https://www.makrel-example.co.uk/
Examples of other wealth managers/IFA's in out industry that we like
https://www.solvirowealth-example.co.uk/
www.lanternQX-example.com
https://orbent-uk-example.com/
https://quentinharrow-example.com/
https://www.velmorwealthplanning-example.co.uk/here-for-you/
https://zrkwealth-example.co.uk/
http://www.dunvix-example.org/
https://www.fenwarrowwealth-example.co.uk/
http://www.unitedcircleofautonomousplanners-example.com/global-membership/
http://www.torquilwealth-example.co.uk/
https://www.keystrelbaxter-example.co.uk/our-values
https://qjtw-example.co.uk/
Target Market(s)
retail customers, professionals.
Industry/Entity Type
uk wealth management
Coding
Coded - Design and coding required
Number of Pages Required
5+ page
Look and feel
Each slider illustrates characteristics of the customer's brand and the style your logo design should communicate.

```html
<!DOCTYPE html>
<html lang="en">
<head>
<meta charset="utf-8">
<title>Pellory Wealth Management</title>
<link href="https://fonts.googleapis.com/css2?family=Cinzel:wght@400;600;700&family=Open+Sans:wght@400;600;700&display=swap" rel="stylesheet">
<style>
:root{
  --teal:#1d5a6a;
  --teal-dark:#174b58;
  --grey:#5e6065;
  --ink:#2a2a2a;
  --body:#3a3a3a;
  --light:#f4f6f7;
  --map:#cfdce1;
  --footer:#1b1b1b;
  --white:#fff;
}
*{box-sizing:border-box;margin:0;padding:0}
html,body{width:1200px;height:4488px;overflow:hidden}
body{font-family:"Open Sans",sans-serif;color:var(--body);background:var(--white);position:relative}
.abs{position:absolute}
.btn{position:absolute;display:flex;align-items:center;justify-content:center;font-family:"Cinzel",serif;font-weight:700;font-size:15px;border-radius:24px;letter-spacing:.5px}
.btn-teal{background:var(--teal);color:var(--white);box-shadow:0 3px 8px rgba(0,0,0,.25)}
.btn-white{background:var(--white);color:var(--teal);box-shadow:0 3px 8px rgba(0,0,0,.2)}

/* header */
.site-header{position:absolute;left:0;top:0;width:1200px;height:118px;background:var(--white)}
.brand{position:absolute;left:111px;top:24px;display:flex;align-items:center;gap:10px}
.brand-dot{width:54px;height:54px;border-radius:50%;border:4px solid var(--teal)}
.brand-name{font-family:"Cinzel",serif;font-weight:600;font-size:24px;color:var(--teal);line-height:1}
.nav{position:absolute;left:362px;top:49px;display:flex;gap:28px;font-size:16px;color:#333}
.nav .active{color:var(--teal)}
.login{left:942px;top:35px;width:146px;height:46px;font-size:14px;background:var(--teal);color:#fff}

/* hero */
.hero{position:absolute;left:0;top:118px;width:1200px;height:740px;overflow:hidden}
.hero-photo{position:absolute;inset:0;background:linear-gradient(100deg,#c9c3b6 0%,#8a8780 30%,#4f5560 55%,#37414d 80%,#2f3a46 100%)}
.hero-wave{position:absolute;left:0;bottom:0;width:1200px;height:140px}
.hero-copy{position:absolute;right:112px;top:160px;text-align:right;color:#fff}
.hero-copy .kicker{font-family:"Cinzel",serif;font-size:32px;letter-spacing:1px}
.hero-copy h1{font-family:"Cinzel",serif;font-weight:600;font-size:52px;line-height:1.2;margin-top:4px}
.hero-copy p{font-size:16px;line-height:26px;margin-top:10px}
.hero-cta{right:112px;top:373px;width:146px;height:44px;font-size:14px}
.hero-arrow{position:absolute;top:337px;width:30px;height:50px}

/* intro */
.intro-title{position:absolute;top:935px;width:1200px;text-align:center;font-family:"Cinzel",serif;font-weight:600;font-size:31px;color:var(--teal)}
.intro-text{position:absolute;top:996px;width:1200px;text-align:center;font-size:15.5px;line-height:26px;color:#333}
.card{position:absolute;top:1092px;width:302px;height:425px;background:#fff;box-shadow:0 4px 14px rgba(0,0,0,.15)}
.card-img{height:233px}
.card-body{position:absolute;left:20px;top:270px;right:20px;border-left:3px solid var(--teal);padding-left:20px}
.card h3{position:absolute;left:42px;top:262px;font-family:"Cinzel",serif;font-weight:700;font-size:17px;color:#222}
.card p{font-size:13.5px;line-height:23px;color:#333;margin-top:26px;height:69px;overflow:hidden}
.card .more{font-family:"Cinzel",serif;font-weight:700;font-size:15px;color:var(--teal);margin-top:6px;display:block}
.slide-btn{position:absolute;top:1283px;width:44px;height:44px;border-radius:50%;display:flex;align-items:center;justify-content:center}

/* company */
.company{position:absolute;left:0;top:1604px;width:1200px;height:600px;background:var(--teal)}
.company-grey{position:absolute;right:0;top:0;width:263px;height:600px;background:var(--grey)}
.company h2{position:absolute;left:111px;top:86px;font-family:"Cinzel",serif;font-weight:600;font-size:30px;color:#fff}
.company p{position:absolute;left:111px;top:148px;width:487px;font-size:15.5px;line-height:25.8px;color:#fff;text-align:justify}
.company .btn{left:111px;top:460px;width:146px;height:44px}
.company-img{position:absolute;left:709px;top:101px;width:380px;height:396px;background:linear-gradient(135deg,#cfe1ea,#6f9fb6 50%,#25465e);box-shadow:0 6px 18px rgba(0,0,0,.3)}

/* process */
.process-title{position:absolute;top:2282px;width:1200px;text-align:center;font-family:"Cinzel",serif;font-weight:600;font-size:30px;color:var(--teal)}
.step{position:absolute;width:124px;height:124px;border-radius:50%;border:4px solid var(--teal);background:#fff;box-shadow:0 0 0 3px #fff,0 0 0 5px #bfc9cc;text-align:center;padding:16px 12px 0}
.step-icon{width:18px;height:18px;border-radius:50%;background:#333;margin:0 auto 3px}
.step-num{font-size:8px;color:#222;font-weight:600;line-height:10px}
.step-name{font-size:8px;color:var(--teal);font-weight:700;line-height:10px}
.step-text{font-size:6px;line-height:7.5px;color:#555;margin-top:3px}

/* portfolio */
.portfolio{position:absolute;left:0;top:2761px;width:1200px;height:600px;background:linear-gradient(90deg,#e9e4d3 0%,#f7f5ee 45%,#f4f2ea 100%)}
.portfolio-img{position:absolute;left:141px;top:96px;width:400px;height:400px;border-radius:50%;border:22px solid var(--teal);background:linear-gradient(135deg,#d7d3cb,#a99e8f 55%,#5b6670)}
.portfolio h2{position:absolute;left:599px;top:89px;font-family:"Cinzel",serif;font-weight:600;font-size:31px;color:var(--teal)}
.portfolio p{position:absolute;left:599px;top:148px;width:486px;font-size:15.5px;line-height:25.8px;color:#333;text-align:justify}
.portfolio .btn{left:599px;top:481px;width:146px;height:44px}

/* contact */
.contact-title{position:absolute;left:111px;top:3440px;font-family:"Cinzel",serif;font-weight:600;font-size:32px;color:var(--teal)}
.field{position:absolute;background:#fff;border:1px solid #e1e1e1;box-shadow:0 2px 6px rgba(0,0,0,.08);font-size:14px;color:#777;padding:0 20px;display:flex;align-items:center}
.field.area{align-items:flex-start;padding-top:18px}
.uk-map{position:absolute;left:705px;top:3447px;width:270px;height:463px;background:var(--map);border-radius:6px}
.map-pin{position:absolute;left:878px;top:3780px}
.map-label{position:absolute;left:927px;top:3783px;font-weight:700;font-size:19px;line-height:26px;color:var(--teal)}

/* footer */
.footer{position:absolute;left:0;top:4018px;width:1200px;height:470px;background:var(--footer);color:#cfcfcf}
.f-brand{position:absolute;left:111px;top:71px;display:flex;align-items:center;gap:14px}
.f-brand .brand-dot{width:92px;height:92px;border:5px solid #fff}
.f-brand span{font-family:"Cinzel",serif;font-weight:600;font-size:30px;color:#fff}
.f-col{position:absolute}
.f-col h4{font-family:"Cinzel",serif;font-weight:700;font-size:17px;color:#fff;margin-bottom:6px}
.f-col li{list-style:none;font-size:13.5px;line-height:24px}
.f-follow{position:absolute;left:111px;top:240px;display:flex;align-items:center;gap:10px;font-family:"Cinzel",serif;font-weight:700;font-size:14px;color:#fff}
.f-follow i{display:block;width:22px;height:22px;border-radius:50%}
.f-copy{position:absolute;right:112px;top:240px;font-size:11.5px}
.f-rule{position:absolute;left:111px;top:284px;width:978px;height:1px;background:#3a3a3a}
.f-legal-title{position:absolute;left:111px;top:306px;font-family:"Cinzel",serif;font-weight:700;font-size:17px;color:#fff}
.f-legal{position:absolute;left:111px;top:348px;width:978px;font-size:12.5px;line-height:24px;color:#ddd;text-align:justify}
</style>
</head>
<body>

<header class="site-header">
  <div class="brand"><div class="brand-dot"></div><div class="brand-name">PELLORY</div></div>
  <nav class="nav">
    <span class="active">Home</span><span>About Us</span><span>Services</span><span>Process</span><span>How We Are Paid</span><span>More ⌄</span>
  </nav>
  <div class="btn login">Client Login</div>
</header>

<section class="hero">
  <div class="hero-photo" role="img" aria-label="Photograph of a wealth adviser in an office reading a tablet"></div>
  <svg class="hero-arrow" style="left:52px" viewBox="0 0 30 50"><path d="M22 8 L8 25 L22 42" fill="none" stroke="#fff" stroke-width="5"/></svg>
  <svg class="hero-arrow" style="right:52px" viewBox="0 0 30 50"><path d="M8 8 L22 25 L8 42" fill="none" stroke="#fff" stroke-width="5"/></svg>
  <div class="hero-copy">
    <div class="kicker">Welcome to</div>
    <h1>Pellory Wealth</h1>
    <p>Lorem ipsum dolor sit amet, consectetur elit, sed do<br>incididunt ut labore et dolore magna aliqua.</p>
  </div>
  <div class="btn btn-teal hero-cta">Contact Us</div>
  <svg class="hero-wave" viewBox="0 0 1200 140" preserveAspectRatio="none">
    <path d="M0 140 L0 60 C300 150 800 140 1200 40 L1200 140 Z" fill="#fff"/>
    <path d="M0 60 C260 110 700 130 1200 40 L1200 75 C800 140 300 155 0 105 Z" fill="#5e6065"/>
    <path d="M0 60 C260 130 700 150 1200 60 L1200 75 C800 150 300 170 0 95 Z" fill="#1d5a6a"/>
  </svg>
</section>

<h2 class="intro-title">Pellory Wealth Management</h2>
<p class="intro-text">Pellory Wealth Management is a privately owned Independent Wealth Management Practice, offering<br>unbiased Financial Planning Services to High Net Worth Private Clients, Corporate Organisations and Trusts</p>

<div class="slide-btn" style="left:39px;background:var(--teal)"><svg width="20" height="14" viewBox="0 0 20 14"><path d="M19 7H2M8 1L2 7l6 6" fill="none" stroke="#fff" stroke-width="2"/></svg></div>
<div class="slide-btn" style="left:1114px;background:var(--grey)"><svg width="20" height="14" viewBox="0 0 20 14"><path d="M1 7h17M12 1l6 6-6 6" fill="none" stroke="#fff" stroke-width="2"/></svg></div>

<article class="card" style="left:111px">
  <div class="card-img" role="img" aria-label="Businessman in a suit with a rising chart" style="background:linear-gradient(135deg,#6a6e7a,#c7b59f 60%,#3d3b40)"></div>
  <h3>Personal Investments</h3>
  <div class="card-body"><p>At Pellory Wealth Management we believe a strong and robust investment process is critical to meeting client's</p><span class="more">Learn More</span></div>
</article>
<article class="card" style="left:449px">
  <div class="card-img" role="img" aria-label="Business professional on the phone against a city skyline" style="background:linear-gradient(135deg,#38434e,#e3a467 45%,#5e6b78)"></div>
  <h3>Personal Planning</h3>
  <div class="card-body"><p>We help our clients identify and address their current and future planning requirements through a process called</p><span class="more">Learn More</span></div>
</article>
<article class="card" style="left:787px">
  <div class="card-img" role="img" aria-label="Two colleagues reviewing a mortgage at a computer" style="background:linear-gradient(135deg,#e9edf0,#9fb0c2 50%,#3d5a86)"></div>
  <h3>Mortgages</h3>
  <div class="card-body"><p>At Pellory Wealth Management we work with specialists in the Mortgage market. We are able to consider all</p><span class="more">Learn More</span></div>
</article>

<section class="company">
  <div class="company-grey"></div>
  <h2>Our Company</h2>
  <p>Pellory Wealth Management is a privately owned Independent Wealth Management Practice, offering Financial Planning Services to High Net Worth Private Clients, Corporate Organisations and Trusts. Our Clients are at the core of our business and we support them in providing unbiased advice, based upon our core principles of integrity, honesty, trust and professionalism. As a firm we aim to partner with leading organisations within their field, who support us in delivering value to our clients. We endeavour to identify and understand our clients specific requirements, to tailor solutions to meet their exact needs and continue to deliver value through developing trusted relationships.</p>
  <div class="btn btn-white">Learn More</div>
  <div class="company-img" role="img" aria-label="Hands holding a tablet with financial data overlay"></div>
</section>

<h2 class="process-title">Our Process</h2>
<svg class="abs" style="left:0;top:2380px" width="1200" height="200" viewBox="0 0 1200 200">
  <g stroke="#333" stroke-width="2">
    <line x1="228" y1="83" x2="292" y2="110"/>
    <line x1="405" y1="110" x2="452" y2="75"/>
    <line x1="566" y1="75" x2="626" y2="110"/>
    <line x1="740" y1="110" x2="803" y2="78"/>
    <line x1="917" y1="78" x2="976" y2="110"/>
  </g>
</svg>
<div class="step" style="left:109px;top:2378px"><div class="step-icon"></div><div class="step-num">STEP 1</div><div class="step-name">ENGAGEMENT</div><div class="step-text">An introductory meeting to explain our services and your goals.</div></div>
<div class="step" style="left:286px;top:2446px"><div class="step-icon"></div><div class="step-num">STEP 2</div><div class="step-name">DISCOVERY</div><div class="step-text">We start to get to fully understand your objectives and needs.</div></div>
<div class="step" style="left:447px;top:2370px"><div class="step-icon"></div><div class="step-num">STEP 3</div><div class="step-name">RESEARCH &amp; ANALYSIS</div><div class="step-text">This is where we develop your Personal Financial Plan for you.</div></div>
<div class="step" style="left:621px;top:2446px"><div class="step-icon"></div><div class="step-num">STEP 4</div><div class="step-name">PRESENT RECOMMENDATIONS</div><div class="step-text">We discuss the Personal Financial Plan and agree the route forward.</div></div>
<div class="step" style="left:798px;top:2373px"><div class="step-icon"></div><div class="step-num">STEP 5</div><div class="step-name">IMPLEMENTATION</div><div class="step-text">Once you fully understand your plan we put it into action.</div></div>
<div class="step" style="left:971px;top:2446px"><div class="step-icon"></div><div class="step-num">STEP 6</div><div class="step-name">ONGOING SERVICE AND RELATIONSHIP</div><div class="step-text">We review your plan regularly so it keeps on track with life.</div></div>
<div class="btn btn-teal" style="left:528px;top:2629px;width:144px;height:44px">View Details</div>

<section class="portfolio">
  <div class="portfolio-img" role="img" aria-label="Two people analysing charts on a tablet over coffee"></div>
  <h2>Portfolio Advisory Service</h2>
  <p>Managing an investment portfolio is a complex process that requires rigorous research and continuous monitoring. One of the investment solutions we offer is our Portfolio Advisory Service (PAS). This is an internal service designed to address these issues, whilst providing high-quality investment portfolio advice to clients who wish for a more informed and controlled approach to portfolio management. Clients will be informed of any suggested alterations to their portfolio holdings and construction and will be required to authorise these changes after a detailed reasoning has been presented to them. We offer a range of portfolios dependent upon the client's appetite to investment risk and ongoing objectives.</p>
  <div class="btn btn-teal">Learn More</div>
</section>

<h2 class="contact-title">Contact Us</h2>
<div class="field" style="left:111px;top:3522px;width:232px;height:58px">Name</div>
<div class="field" style="left:352px;top:3522px;width:231px;height:58px">Email</div>
<div class="field" style="left:111px;top:3599px;width:232px;height:58px">Phone</div>
<div class="field" style="left:352px;top:3599px;width:231px;height:58px;justify-content:space-between">Address<span style="font-size:11px">⌄</span></div>
<div class="field area" style="left:111px;top:3675px;width:472px;height:111px">Message</div>
<div class="btn btn-teal" style="left:113px;top:3816px;width:120px;height:46px">Submit</div>
<div class="uk-map" role="img" aria-label="Map of the United Kingdom marking the office location"></div>
<svg class="map-pin" width="30" height="42" viewBox="0 0 30 42"><path d="M15 1C7 1 1 7 1 15c0 10 14 26 14 26s14-16 14-26C29 7 23 1 15 1z" fill="#1d5a6a"/><circle cx="15" cy="15" r="6" fill="#fff"/></svg>
<div class="map-label">Pellory Wealth<br>Management</div>

<footer class="footer">
  <div class="f-brand"><div class="brand-dot"></div><span>PELLORY</span></div>
  <div class="f-col" style="left:394px;top:42px"><h4>Links</h4><ul><li>Home</li><li>About Us</li><li>Services</li><li>Process</li><li>How We Are Paid</li><li>Portfolio Advisory Service</li><li>Knowledge Centre</li><li>Contact Us</li></ul></div>
  <div class="f-col" style="left:608px;top:42px"><h4>Contact</h4><ul><li style="color:#fff">Call</li><li style="line-height:14px">01632 960418</li><li style="margin-top:12px;color:#fff">Email</li><li style="line-height:14px">office@pellorywealth-example.com</li></ul></div>
  <div class="f-col" style="left:845px;top:38px"><h4>Our Services</h4><ul><li>Personal Investments</li><li>Personal Planning</li><li>Corporate Financial Planning</li><li>Mortgages</li></ul></div>
  <div class="f-follow">FOLLOWS <i style="background:#c13584;margin-left:8px"></i><i style="background:#3b66c4"></i><i style="background:#e52d27"></i></div>
  <div class="f-copy">Copyright © 2022 All Rights Reserved</div>
  <div class="f-rule"></div>
  <div class="f-legal-title">Pellory Wealth Management</div>
  <p class="f-legal">The guidance provided within this website is subject to the UK regulatory regime and is therefore primarily targeted at consumers based in the UK. Pellory Wealth Management Limited is an appointed representative of Verancore Connect Limited, which is authorised and regulated by the Financial Oversight Authority. Verancore Connect Ltd is entered on the Financial services Register (www.fo-authority-example.org.uk/register) under reference 482917.</p>
</footer>

</body>
</html>
```